Selam-Kaveh - Promote and Support a community

Design a website for Ethiopean Community. the design should be friendly, easy to navigate and maintain the look & feel of the Ethiopian culture. a proposed logo is attached but it can be change according to your recommendations. This is a project we are doing at a discount rate as it supports a weak community.
Please visit their current website http://www.selam-kaveh.example.org/index.php?lang=en

Target Market(s)

Community members, potential doners

Industry/Entity Type

community

Number of Pages Required

1 page

Font styles to use
Sans Serif

Requirements
Must have
• easy to navigate friendly interface

```html
<!DOCTYPE html>
<html lang="en">
<head>
<meta charset="utf-8">
<title>Selam-Kaveh – Promote and Support a Community</title>
<link rel="stylesheet" href="https://fonts.googleapis.com/css2?family=Poppins:wght@400;500;600;700&family=Roboto:wght@400;500&display=swap">
<style>
:root{
  --green:#1f7a4f;
  --green-dark:#135c39;
  --green-deep:#0f4a2d;
  --ink:#111;
  --text:#333;
  --muted:#777;
  --line:#e6e6e6;
  --white:#fff;
  --black:#000;
}
*{margin:0;padding:0;box-sizing:border-box}
html,body{width:1200px;height:3352px;overflow:hidden}
body{position:relative;font-family:"Roboto",sans-serif;color:var(--text);background:var(--white)}
a{color:inherit;text-decoration:none}
.abs{position:absolute}

/* header */
.site-header{position:absolute;top:0;left:0;width:1200px;height:110px;border-bottom:1px solid var(--line);background:var(--white)}
.brand{position:absolute;left:112px;top:14px;display:flex;align-items:center;gap:8px;font-family:"Poppins",sans-serif;font-weight:600;font-size:15px;color:var(--green-dark)}
.brand-dot{width:22px;height:22px;border-radius:50%;background:var(--green)}
.header-divider{position:absolute;left:234px;top:0;width:1px;height:110px;background:var(--line)}
.topbar{position:absolute;left:264px;top:14px;width:824px;height:36px;border-bottom:1px solid var(--line);font-family:"Poppins",sans-serif;font-size:15px;color:#222}
.topbar span{position:absolute;top:0;display:flex;align-items:center;gap:9px}
.topbar svg{fill:var(--green)}
.topbar .tag::after{content:"";position:absolute;left:0;top:34px;width:40px;height:3px;background:var(--green)}
.main-nav{position:absolute;left:265px;top:70px;display:flex;gap:37px;font-family:"Poppins",sans-serif;font-size:15px;color:#222;letter-spacing:.3px}

/* hero */
.hero{position:absolute;top:110px;left:0;width:1200px;height:640px;overflow:hidden}
.hero-photo{position:absolute;inset:0;background:linear-gradient(180deg,#6f7c8a 0%,#8a8a6a 18%,#5d6a2e 35%,#4c5f22 60%,#2f3c16 100%)}
.hero-shade{position:absolute;inset:0;background:rgba(0,0,0,.25)}
.hero-title{position:absolute;top:198px;width:100%;text-align:center;font-family:"Poppins",sans-serif;font-weight:600;font-size:42px;letter-spacing:2px;color:var(--white)}
.hero-sub{position:absolute;top:262px;left:300px;width:600px;text-align:center;font-size:15px;line-height:26px;letter-spacing:.5px;color:var(--white)}
.btn{display:inline-block;font-family:"Poppins",sans-serif;font-weight:600;border-radius:26px;text-align:center}
.btn-green{background:linear-gradient(90deg,var(--green),var(--green-dark));color:var(--white)}
.hero .btn{position:absolute;left:516px;top:340px;width:169px;height:52px;line-height:52px;font-size:15px;letter-spacing:.8px}
.dots{position:absolute;top:536px;left:556px;display:flex;gap:5px}
.dots i{width:13px;height:13px;border-radius:50%;background:var(--white)}
.dots i.off{background:transparent;border:2px solid var(--white)}
.hero-curve{position:absolute;left:0;top:560px}

/* about */
.about-photo{position:absolute;left:113px;top:826px;width:375px;height:375px;border-radius:50%;background:radial-gradient(circle at 50% 55%,#8a4a3a 0%,#9b7a5e 40%,#7a6048 75%,#5d4a3a 100%)}
.about-ring{position:absolute;left:124px;top:836px;width:376px;height:376px;border-radius:50%;background:var(--green)}
.about-text{position:absolute;left:562px;top:816px;width:522px}
.section-h{font-family:"Poppins",sans-serif;font-weight:600;color:var(--ink)}
.about-text h2{font-size:35px;letter-spacing:1px;margin-bottom:18px}
.about-text p{font-size:15px;line-height:25.8px;letter-spacing:.5px;color:#333}
.about-text .btn{margin-top:24px;width:170px;height:52px;line-height:52px;font-size:15px;letter-spacing:.8px}

/* health band */
.health{position:absolute;left:0;top:1295px;width:1200px;height:490px}
.health-content{position:absolute;left:0;top:0;width:1200px;text-align:center;color:var(--white)}
.health h2{position:absolute;top:82px;width:100%;font-family:"Poppins",sans-serif;font-weight:600;font-size:36px;letter-spacing:2px}
.health p{position:absolute;top:155px;left:148px;width:904px;font-size:15px;line-height:25.8px;letter-spacing:.6px}
.btn-white{background:var(--white);color:var(--green-dark)}
.health .btn{position:absolute;left:516px;top:336px;width:170px;height:52px;line-height:52px;font-size:15px;letter-spacing:.8px}

/* news */
.news-title{position:absolute;top:1855px;width:1200px;text-align:center;font-size:35px}
.card{position:absolute;background:var(--white);box-shadow:0 2px 10px rgba(0,0,0,.16)}
.card-img{position:absolute}
.card h3{font-family:"Poppins",sans-serif;font-weight:500;color:var(--ink)}
.card .date{display:flex;align-items:center;gap:8px;font-size:15px;color:var(--muted)}
.card .date svg{fill:var(--green)}
.card p{font-size:14.5px;line-height:26px;color:#222}
.card .more{font-family:"Poppins",sans-serif;font-weight:600;font-size:13.5px;color:var(--green-dark)}
.card-lg{left:116px;top:1948px;width:482px;height:518px}
.card-lg .card-img{left:12px;top:12px;width:460px;height:316px;background:linear-gradient(180deg,#5f7a4a 0%,#7f8e5a 45%,#9a8f76 70%,#6d6250 100%)}
.card-lg .body{position:absolute;left:16px;top:350px;width:440px}
.card-lg h3{font-size:20.5px;margin-bottom:14px}
.card-lg .date{margin-bottom:9px}
.card-lg p{margin-bottom:6px}
.card-sm{left:624px;width:471px;height:250px}
.card-sm .card-img{left:12px;top:12px;width:224px;height:226px}
.card-sm .body{position:absolute;left:254px;top:20px;width:205px}
.card-sm h3{font-size:21px;line-height:30px;margin-bottom:14px}
.card-sm .date{margin-bottom:8px}
.card-sm p{margin-bottom:6px}

/* partners */
.partners-title{position:absolute;top:2552px;width:1200px;text-align:center;font-size:35px}
.partners-intro{position:absolute;top:2623px;left:290px;width:620px;text-align:center;font-size:15px;line-height:26px;color:#444}
.partner{position:absolute;background:#e6efe9;border-radius:6px}

/* footer */
.footer-curve{position:absolute;left:0;top:2895px}
.site-footer{position:absolute;left:0;top:2960px;width:1200px;height:392px;background:var(--black);color:var(--white)}
.f-col{position:absolute;top:60px}
.f-col h4{font-family:"Poppins",sans-serif;font-weight:600;font-size:17px;padding-bottom:12px;position:relative;margin-bottom:20px}
.f-col h4::after{content:"";position:absolute;left:0;bottom:0;width:32px;height:2px;background:var(--green)}
.f-col li{list-style:none;font-size:15px;line-height:30px;display:flex;align-items:flex-start;gap:9px}
.f-col li svg{flex:none;margin-top:9px;fill:var(--green)}
.f-col.help li svg,.f-col.follow li svg{fill:var(--white)}
.f-field{width:243px;border-bottom:1px solid #666;font-size:14.5px;color:#bbb;padding:0 0 12px 2px;margin-bottom:22px}
.f-col .btn{margin-top:12px;width:160px;height:42px;line-height:42px;font-size:15px;box-shadow:0 0 14px rgba(31,122,79,.6)}
.copyright{position:absolute;left:0;top:355px;width:1200px;text-align:center;font-size:15px;color:#ddd}
.footer-rule{position:absolute;left:112px;top:305px;width:976px;height:1px;background:#222}
</style>
</head>
<body>

<header class="site-header">
  <div class="brand"><span class="brand-dot"></span>Selam-Kaveh</div>
  <div class="header-divider"></div>
  <div class="topbar">
    <span class="tag" style="left:0">Lorem ipsum dolor sit amet</span>
    <span style="left:294px"><svg width="15" height="15" viewBox="0 0 24 24"><path d="M6.6 10.8a15 15 0 0 0 6.6 6.6l2.2-2.2c.3-.3.7-.4 1-.2 1.1.4 2.3.6 3.6.6.6 0 1 .4 1 1V20c0 .6-.4 1-1 1A17 17 0 0 1 3 4c0-.6.4-1 1-1h3.5c.6 0 1 .4 1 1 0 1.3.2 2.5.6 3.6.1.3 0 .7-.2 1z"/></svg>155-010-4477</span>
    <span style="left:514px"><svg width="16" height="13" viewBox="0 0 24 18"><path d="M0 2l12 8 12-8V0H0zM0 5v13h24V5l-12 8z"/></svg>hello@selamkaveh.example.org</span>
  </div>
  <nav class="main-nav">
    <a>Home</a><a>About</a><a>The Community</a><a>Programs</a><a>News</a><a>Advocacy</a><a>Partners</a><a>Support Us</a>
  </nav>
</header>

<section class="hero">
  <div class="hero-photo" role="img" aria-label="Panorama of green terraced Ethiopian highlands under a hazy sky"></div>
  <div class="hero-shade"></div>
  <h1 class="hero-title">Welcome to Selam-Kaveh</h1>
  <p class="hero-sub">Lorem ipsum dolor sit amet, consectetur adipiscing elit, sed do eiusmod tempor incididunt ut labore et dolore magna aliqua.</p>
  <a class="btn btn-green">Get Started</a>
  <div class="dots"><i></i><i class="off"></i><i></i><i></i><i></i></div>
  <svg class="hero-curve" width="1200" height="80" viewBox="0 0 1200 80">
    <path d="M0 15 Q600 110 1200 15 L1200 80 L0 80Z" fill="#1f7a4f"/>
    <path d="M0 38 Q600 150 1200 38 L1200 80 L0 80Z" fill="#fff"/>
  </svg>
</section>

<section class="about">
  <div class="about-ring"></div>
  <div class="about-photo" role="img" aria-label="Two young girls in colourful dresses sitting together on rocky ground"></div>
  <div class="about-text">
    <h2 class="section-h">About Selam Kaveh</h2>
    <p>Aliyah (immigration) from Ethiopia to Israel and the transition to a sedentary lifestyle has resulted in the emergence of chronic diseases, in particular diabetes. While only 0.4% of the new immigrants were diagnosed with Type 2 diabetes upon arrival, by the time they had lived in Israel for ten years the figure had risen to 18% - three times as many as in the general population. The incidence of hypertension, obesity, asthma and Type 1 diabetes had also increased dramatically. Selam Kaveh was founded in 1999 by Dr. Miriam Oren, Head of the Endocrinology Unit at the Carmel Valley Medical Center.</p>
    <a class="btn btn-green">Learn More</a>
  </div>
</section>

<section class="health">
  <svg class="abs" style="left:0;top:0" width="1200" height="490" viewBox="0 0 1200 490" role="img" aria-label="Green-tinted view of rolling hills">
    <defs><linearGradient id="healthBg" x1="0" y1="0" x2="0" y2="1"><stop offset="0" stop-color="#2a7f57"/><stop offset=".55" stop-color="#22754c"/><stop offset="1" stop-color="#1a6a40"/></linearGradient></defs>
    <path d="M0 60 Q600 -40 1200 60 L1200 428 Q600 530 0 428Z" fill="url(#healthBg)"/>
  </svg>
  <div class="health-content">
    <h2>Health &amp; Community</h2>
    <p>Today the Ethiopian Israeli community numbers over 120,000 with new immigrants still continuing to arrive. For many, immigration led to the disintegration of traditional family and social structures with traumatic results for the community and further impeding absorption into Israeli society.A report issued in 2008 by the Prime Minister's Office states that 68% of Ethiopian families live under the poverty line and the Meridian Policy Centre advises that "Ethiopian immigrants ranked lowest on the quality of life index, which considers per-capita income, per-room housing density and basic</p>
    <a class="btn btn-white">Learn More</a>
  </div>
</section>

<h2 class="section-h news-title">Selam Kaveh in the News</h2>

<article class="card card-lg">
  <div class="card-img" role="img" aria-label="Villagers in traditional shawls walking along a dirt road lined with trees"></div>
  <div class="body">
    <h3>Lorem ipsum dolor sit amet, consectetur</h3>
    <div class="date"><svg width="15" height="15" viewBox="0 0 16 16"><path d="M2 3h12v12H2zM3 6v8h10V6zM4 1h2v3H4zM10 1h2v3h-2z"/></svg>March 2002</div>
    <p>Lorem ipsum dolor sit amet, consectetur adipiscing elit, sed do eiusmod tempor incididunt ut labore et dolore</p>
    <a class="more">Learn More</a>
  </div>
</article>

<article class="card card-sm" style="top:1948px">
  <div class="card-img" role="img" aria-label="Smiling child carrying a woven basket on her head" style="background:linear-gradient(180deg,#9a8f80 0%,#a8886a 40%,#7a3a34 75%,#5a3030 100%)"></div>
  <div class="body">
    <h3>Lorem ipsum dolor sit</h3>
    <div class="date"><svg width="15" height="15" viewBox="0 0 16 16"><path d="M2 3h12v12H2zM3 6v8h10V6zM4 1h2v3H4zM10 1h2v3h-2z"/></svg>March 2002</div>
    <p>Lorem ipsum dolor sit amet, consectetur adipiscing elit, sed do eiusmod tempor</p>
    <a class="more">Learn More</a>
  </div>
</article>

<article class="card card-sm" style="top:2218px">
  <div class="card-img" role="img" aria-label="Stack of brightly coloured woven baskets at a market" style="background:linear-gradient(135deg,#c43a6a 0%,#d88a3a 35%,#3a8ac4 65%,#c4b05a 100%)"></div>
  <div class="body">
    <h3>Lorem ipsum dolor sit</h3>
    <div class="date"><svg width="15" height="15" viewBox="0 0 16 16"><path d="M2 3h12v12H2zM3 6v8h10V6zM4 1h2v3H4zM10 1h2v3h-2z"/></svg>March 2002</div>
    <p>Lorem ipsum dolor sit amet, consectetur adipiscing elit, sed do eiusmod tempor</p>
    <a class="more">Learn More</a>
  </div>
</article>

<h2 class="section-h partners-title">Our Partners</h2>
<p class="partners-intro">Lorem ipsum dolor sit amet, consectetur adipiscing elit, sed do eiusmod tempor incididunt ut labore et dolore magna aliqua. Quis ipsum suspendisse ultrices gravida.</p>
<div class="partner" style="left:134px;top:2735px;width:130px;height:38px"></div>
<div class="partner" style="left:330px;top:2715px;width:188px;height:72px;background:#fff;box-shadow:0 2px 10px rgba(0,0,0,.15)"><div class="partner" style="left:30px;top:20px;width:128px;height:32px"></div></div>
<div class="partner" style="left:598px;top:2715px;width:96px;height:72px"></div>
<div class="partner" style="left:776px;top:2715px;width:126px;height:72px"></div>
<div class="partner" style="left:978px;top:2712px;width:64px;height:100px;border-radius:4px"></div>

<svg class="footer-curve" width="1200" height="70" viewBox="0 0 1200 70">
  <path d="M0 82 Q600 -50 1200 82Z" fill="#1f7a4f"/>
  <path d="M0 70 Q600 -25 1200 70Z" fill="#000"/>
</svg>
<footer class="site-footer">
  <div class="f-col" style="left:112px">
    <h4>Contact</h4>
    <ul>
      <li><svg width="10" height="13" viewBox="0 0 10 14"><path d="M5 0a5 5 0 0 0-5 5c0 4 5 9 5 9s5-5 5-9a5 5 0 0 0-5-5zm0 7a2 2 0 1 1 0-4 2 2 0 0 1 0 4z"/></svg><span>Lorem ipsum dolor<br>sit amet</span></li>
      <li style="margin-top:6px"><svg width="12" height="12" viewBox="0 0 24 24"><path d="M6.6 10.8a15 15 0 0 0 6.6 6.6l2.2-2.2c.3-.3.7-.4 1-.2 1.1.4 2.3.6 3.6.6.6 0 1 .4 1 1V20c0 .6-.4 1-1 1A17 17 0 0 1 3 4c0-.6.4-1 1-1h3.5c.6 0 1 .4 1 1 0 1.3.2 2.5.6 3.6.1.3 0 .7-.2 1z"/></svg>155-010-4477</li>
      <li style="margin-top:8px"><svg width="13" height="10" viewBox="0 0 24 18"><path d="M0 2l12 8 12-8V0H0zM0 5v13h24V5l-12 8z"/></svg>selamkaveh.example.org</li>
    </ul>
  </div>
  <div class="f-col help" style="left:366px">
    <h4>Help Link</h4>
    <ul>
      <li><svg width="7" height="10" viewBox="0 0 7 10"><path d="M1 0l6 5-6 5-1-1 5-4-5-4z"/></svg>Terms&amp;condtions</li>
      <li><svg width="7" height="10" viewBox="0 0 7 10"><path d="M1 0l6 5-6 5-1-1 5-4-5-4z"/></svg>Privacy Policy</li>
      <li><svg width="7" height="10" viewBox="0 0 7 10"><path d="M1 0l6 5-6 5-1-1 5-4-5-4z"/></svg>About Us</li>
      <li><svg width="7" height="10" viewBox="0 0 7 10"><path d="M1 0l6 5-6 5-1-1 5-4-5-4z"/></svg>Support</li>
    </ul>
  </div>
  <div class="f-col follow" style="left:627px">
    <h4>Follow us</h4>
    <ul>
      <li><svg width="10" height="10" viewBox="0 0 10 10"><circle cx="5" cy="5" r="4"/></svg>Community Wall</li>
      <li><svg width="10" height="10" viewBox="0 0 10 10"><circle cx="5" cy="5" r="4"/></svg>Photo Stream</li>
      <li><svg width="10" height="10" viewBox="0 0 10 10"><circle cx="5" cy="5" r="4"/></svg>Short Posts</li>
      <li><svg width="10" height="10" viewBox="0 0 10 10"><circle cx="5" cy="5" r="4"/></svg>Video Channel</li>
    </ul>
  </div>
  <div class="f-col" style="left:842px">
    <h4>Newsletter updates</h4>
    <div class="f-field" style="margin-top:-4px">Name*</div>
    <div class="f-field">Email*</div>
    <a class="btn btn-green">Submit Now</a>
  </div>
  <div class="footer-rule"></div>
  <p class="copyright">© 2022 Selam Kaveh All Rights Reserved</p>
</footer>

</body>
</html>
```